Real Estate Investor needs awesome business card design

I invest in real estate, focused on multi-family properties, and I need a business card to hand out to potential partners. I prefer simple, clean designs, but it needs to stand out, so I'd like there to be a bit of red in the design as well.

It should include this information:

Front
Dallin Pecksworth
Real Estate Investor
Direct phone: 502-867-3394
Email: dallinhpecksworth@quillmail.example
Headshot (Picture), I've uploaded a few, just pick the one you think looks best with your design. You can remove the background from the headshot image if it looks better.

Back
The back of the card's design should flow and be congruent with the front. On the back I want to put an inspirational quote or question. There will be different ones depending on the card, so I'll need the original file so I can edit it in the end.

For now, use “The Pessimist Sees Difficulty In Every Opportunity. The Optimist Sees The Opportunity In Every Difficulty.” -Barnaby Ellsworth

Target Market(s)

Investors

Industry/Entity Type

Real Estate

Contact Information for Business Card

Front
Dallin Pecksworth
Real Estate Investor

Back
The back of the card's design should flow and be congruent with the front. On the back I want to put an inspirational quote or question. There will be different ones depending on the card, so I'll need the original file so I can edit it in the end. I've uploaded some EXAMPLES of business cards with quotes on them. Don't copy but feel free to use them as inspiration.

The design will be printed on "ZIB sized" business cards
1039 x 697 pixels
with rounded corners

Font styles to use
Serif
Decorative
Script

Colors
ec1f27

Requirements
Must have
• Headshot, name, and other information in it.
• 1039 x 697 pixels
• Rounded corners
• Clean design that pops. I'm open to see any color background, including black.
• Headshots can be located here: https://www.filecrate.example/sh/8kd2wq7mzt31hvx/BBQTXP4ruf9LmQ0KhcvWx7b?dl=0
Nice to have
• It would be awesome if the design included a personal signature or monogram, but if not I'll get a personal logo developed later and the card redesigned if I think it needs it.
Should not have
• Cluttered design

```html
<!DOCTYPE html>
<html lang="en">
<head>
<meta charset="utf-8">
<title>Dallin Pecksworth – Business Card</title>
<link rel="stylesheet" href="https://fonts.googleapis.com/css2?family=Open+Sans:wght@400;600;700&family=Jost:wght@400;600&family=Libre+Baskerville:ital,wght@1,700&display=swap">
<style>
  :root {
    --stage: #e9e6e2;
    --card-white: #ffffff;
    --ink: #24273a;
    --ink-soft: #4a4d5c;
    --navy: #252839;
    --on-navy: #ffffff;
    --accent-red: #ec1f27;
    --photo-light: #f3eee9;
    --photo-skin: #d9b49c;
    --photo-suit: #2b2f45;
  }
  * { box-sizing: border-box; margin: 0; padding: 0; }
  html, body {
    width: 1200px; height: 987px; overflow: hidden;
    background: var(--stage);
  }
  .canvas { position: relative; width: 1200px; height: 987px; }

  .card {
    position: absolute;
    left: 307px;
    width: 587px;
    height: 393px;
    overflow: hidden;
  }
  .card--front { top: 103px; background: var(--card-white); }
  .card--back  { top: 520px; background: var(--navy); }

  .identity {
    position: absolute;
    z-index: 2;
    left: 43px;
    top: 46px;
    font-family: "Open Sans", sans-serif;
    color: var(--ink);
    white-space: nowrap;
  }
  .identity__name {
    font-size: 21px;
    font-weight: 600;
    letter-spacing: 0.2px;
    text-transform: uppercase;
    line-height: 1.1;
  }
  .identity__role {
    font-size: 15px;
    color: var(--ink-soft);
    margin-top: 2px;
  }
  .contact { list-style: none; margin-top: 16px; }
  .contact__item {
    display: flex;
    align-items: center;
    gap: 9px;
    font-size: 15px;
    color: var(--ink-soft);
    line-height: 24px;
  }
  .contact__icon { width: 14px; height: 14px; fill: var(--ink); flex: none; }

  .headshot {
    position: absolute;
    z-index: 1;
    right: 0;
    top: 0;
    width: 300px;
    height: 393px;
    background:
      radial-gradient(ellipse 40% 40% at 58% 42%, var(--photo-skin) 0%, rgba(217,180,156,0.55) 55%, rgba(243,238,233,0) 100%),
      radial-gradient(ellipse 70% 30% at 60% 108%, var(--photo-suit) 0%, var(--photo-suit) 55%, rgba(43,47,69,0) 100%),
      linear-gradient(90deg, rgba(243,238,233,0) 0%, var(--photo-light) 35%, var(--photo-light) 100%);
  }

  .quote {
    position: absolute;
    inset: 0;
    display: flex;
    flex-direction: column;
    align-items: center;
    justify-content: center;
    text-align: center;
    color: var(--on-navy);
    padding-top: 6px;
  }
  .quote__text {
    font-family: "Jost", sans-serif;
    font-size: 23px;
    font-weight: 400;
    line-height: 31px;
  }
  .quote__mark { font-weight: 600; font-size: 26px; color: var(--accent-red); }
  .quote__author {
    font-family: "Libre Baskerville", serif;
    font-style: italic;
    font-weight: 700;
    font-size: 14px;
    margin-top: 6px;
  }
</style>
</head>
<body>
<main class="canvas">
  <section class="card card--front" aria-label="Card front">
    <div class="identity">
      <h1 class="identity__name">Dallin Pecksworth</h1>
      <p class="identity__role">Real Estate Investor</p>
      <ul class="contact">
        <li class="contact__item">
          <svg class="contact__icon" viewBox="0 0 24 24" aria-hidden="true"><path d="M6.6 10.8a15.1 15.1 0 0 0 6.6 6.6l2.2-2.2c.3-.3.7-.4 1-.2 1.1.4 2.3.6 3.6.6.6 0 1 .4 1 1V20c0 .6-.4 1-1 1C10.6 21 3 13.4 3 4c0-.6.4-1 1-1h3.5c.6 0 1 .4 1 1 0 1.3.2 2.5.6 3.6.1.3 0 .7-.2 1z"/></svg>
          <span>502-867-3394</span>
        </li>
        <li class="contact__item">
          <svg class="contact__icon" viewBox="0 0 24 24" aria-hidden="true"><path d="M2 5h20v14H2z M3.5 6.5v.4l8.5 6 8.5-6v-.4z" fill-rule="evenodd"/><path d="M3.5 8.6v8.9h17V8.6L12 14.6z" fill="#fff"/></svg>
          <span>dallinhpecksworth@quillmail.example</span>
        </li>
      </ul>
    </div>
    <div class="headshot" role="img" aria-label="Headshot of Dallin Pecksworth in a dark suit and white shirt on a light background"></div>
  </section>

  <section class="card card--back" aria-label="Card back">
    <blockquote class="quote">
      <p class="quote__text"><span class="quote__mark">“</span>The Pessimist Sees Difficulty<br>In Every Opportunity.<br>The Optimist Sees The Opportunity<br>In Every Difficulty.<span class="quote__mark">”</span></p>
      <cite class="quote__author">Barnaby Ellsworth</cite>
    </blockquote>
  </section>
</main>
</body>
</html>
```